K&T Power Depot Business Cards

This will be used a business cards. Would love an industrial type flavor paired with the floating/3d is design like attached.

Do not have any certain colors picked out but something that will look good and stand out!!!.

K&T Power Depot
"Don't be left in the dark"

The business does home standby Generators..

Contact Information for Business Card

K&T Power Depot

Requirements
Must have
• Would love an industrial type flavor paired with the floating/3d is design like attached for a sample.

```html
<!DOCTYPE html>
<html lang="en">
<head>
<meta charset="utf-8">
<title>K&amp;T Power Depot – Business Cards</title>
<link href="https://fonts.googleapis.com/css2?family=Montserrat:wght@600;700&family=Varela+Round&family=Arimo:wght@400&display=swap" rel="stylesheet">
<style>
  :root {
    --backdrop: #2a2a2a;
    --card: #0b0b0b;
    --brand-blue: #0a5289;
    --brand-green: #8cc21f;
    --text-light: #d6d6d6;
    --text-muted: #a8a8a8;
    --rule: #4a4a4a;
  }
  * { margin: 0; padding: 0; box-sizing: border-box; }
  html, body { width: 1200px; height: 900px; overflow: hidden; }
  body {
    background: radial-gradient(ellipse at 50% 40%, #343434 0%, var(--backdrop) 70%, #1c1c1c 100%);
    position: relative;
    font-family: "Arimo", Arial, sans-serif;
  }
  .card {
    position: absolute;
    width: 540px;
    height: 309px;
    background: var(--card);
    box-shadow: 0 18px 40px rgba(0,0,0,.6);
  }
  .card--back { left: 600px; top: 110px; }
  .card--front { left: 60px; top: 480px; }

  .brand-name {
    font-family: "Montserrat", sans-serif;
    font-weight: 700;
    color: var(--brand-blue);
    letter-spacing: .5px;
    text-transform: uppercase;
    white-space: nowrap;
  }
  .tagline {
    font-family: "Varela Round", sans-serif;
    color: var(--brand-green);
    white-space: nowrap;
  }

  /* back */
  .card--back .brand-lockup {
    position: absolute; left: 0; right: 0; top: 92px; text-align: center;
  }
  .card--back .brand-name { font-size: 36px; line-height: 1.1; }
  .card--back .tagline { font-size: 20px; margin-top: 6px; }
  .partner-list {
    position: absolute; left: 0; right: 0; top: 218px;
    text-align: center; font-size: 13px; color: var(--text-muted); letter-spacing: .3px;
  }
  .partner-list .sep { margin: 0 8px; }

  /* front */
  .card--front .brand-lockup {
    position: absolute; right: 70px; top: 48px; text-align: right;
  }
  .card--front .brand-name { font-size: 30px; line-height: 1.1; }
  .card--front .tagline { font-size: 17px; margin-top: 6px; }
  .card--front .divider {
    position: absolute; left: 130px; right: 24px; top: 184px;
    height: 1px; background: var(--rule);
  }
  .person { position: absolute; left: 48px; top: 150px; }
  .person__name {
    font-family: "Montserrat", sans-serif; font-weight: 600;
    font-size: 20px; line-height: 24px; text-transform: uppercase; letter-spacing: .3px;
  }
  .person__first { color: var(--brand-blue); }
  .person__last { color: var(--brand-green); }
  .person__role { font-size: 14px; color: var(--text-light); margin-top: 2px; }
  .contact-list {
    position: absolute; left: 66px; top: 214px; list-style: none;
    font-size: 14px; color: var(--text-light);
  }
  .contact-list li { display: flex; align-items: center; gap: 8px; height: 22px; }
  .contact-icon { width: 17px; height: 17px; flex: none; }
  .contact-list .accent { color: var(--brand-green); }
</style>
</head>
<body>

<section class="card card--back" aria-label="Business card back">
  <div class="brand-lockup">
    <div class="brand-name">K&amp;T Power Depot</div>
    <div class="tagline">Don't be left in the dark</div>
  </div>
  <div class="partner-list">
    Genvora<span class="sep">|</span>Kelstad<span class="sep">|</span>Brannock And Shaw<span class="sep">|</span>Dunmeral
  </div>
</section>

<section class="card card--front" aria-label="Business card front">
  <div class="brand-lockup">
    <div class="brand-name">K&amp;T Power Depot</div>
    <div class="tagline">Don't be left in the dark</div>
  </div>
  <div class="divider"></div>

  <div class="person">
    <div class="person__name"><span class="person__first">Daniel</span> <span class="person__last">Hayes</span></div>
    <div class="person__role">Owner</div>
  </div>

  <ul class="contact-list">
    <li>
      <svg class="contact-icon" viewBox="0 0 20 20" aria-hidden="true">
        <circle cx="10" cy="10" r="10" fill="#8cc21f"/>
        <path d="M6.5 5.5l2 .2.8 2.3-1.2 1a6 6 0 0 0 3 3l1-1.2 2.3.8.2 2c-.3.6-1 1-1.7.9C9.5 14.2 5.8 10.5 5.5 7.2c0-.7.4-1.4 1-1.7z" fill="#0b0b0b"/>
      </svg>
      555-014-2297
    </li>
    <li>
      <svg class="contact-icon" viewBox="0 0 20 20" aria-hidden="true">
        <circle cx="10" cy="10" r="10" fill="#8cc21f"/>
        <rect x="5" y="6.5" width="10" height="7" fill="#0b0b0b"/>
        <path d="M5 6.5l5 4 5-4" stroke="#8cc21f" stroke-width="1" fill="none"/>
      </svg>
      sales@ktpowerdepot.com
    </li>
    <li>
      <svg class="contact-icon" viewBox="0 0 20 20" aria-hidden="true">
        <circle cx="10" cy="10" r="10" fill="#8cc21f"/>
        <g fill="none" stroke="#0b0b0b" stroke-width="1.1">
          <circle cx="10" cy="10" r="5"/>
          <ellipse cx="10" cy="10" rx="2.2" ry="5"/>
          <path d="M5 10h10M6 7.5h8M6 12.5h8"/>
        </g>
      </svg>
      <span>www.<span class="accent">ktpowerdepot</span>.com</span>
    </li>
  </ul>
</section>

</body>
</html>
```